Classy business card for accounting firm

We're looking for a new business card for our accounting firm. Our logo was designed by Brandolith, so all of the design info we would like to use has been provided. The specific font provided isn't required to be used.

We want the card to look classy and elegent. Probably more minimalistic, but still with some pops of color.

The options we would like to include on the card are as follows:
1. Main office phone line
2. Direct phone line
3. Email address
4. Website URL
5. Name
6. Title (CEO, President, etc.)
7. Firm Address

The design and card should be double sided!!! The drop down box in the project brief for some reason is defaulting to single sided. Not sure why this is happening.

Thanks!

Contact Information for Business Card

The options we would like to include on the card are as follows: 1. Main office phone line 2. Direct phone line 3. Email address 4. Website URL 5. Name 6. Title (CEO, President, etc.) 7. Firm Address

Requirements
Must have
• Card must be double sided.

```html
<!DOCTYPE html>
<html lang="en">
<head>
<meta charset="utf-8">
<title>Northfield Tax Group — Business Card</title>
<link href="https://fonts.googleapis.com/css2?family=Nunito+Sans:wght@400;600;700&family=Arimo:wght@400;700&display=swap" rel="stylesheet">
<style>
  :root {
    --canvas: #e6e6e6;
    --card: #333333;
    --edge: #f07d0c;
    --orange: #f28a12;
    --green: #8cc63f;
    --ink: #f2f2f2;
    --muted: #bdbdbd;
  }
  * { box-sizing: border-box; margin: 0; padding: 0; }
  html, body { width: 1200px; height: 900px; overflow: hidden; }
  body {
    background: var(--canvas);
    display: flex; flex-direction: column; align-items: center; justify-content: center;
    gap: 56px;
    font-family: "Nunito Sans", sans-serif;
  }
  .card {
    position: relative;
    width: 620px; height: 354px;
    border-radius: 22px;
    background: var(--card);
    border-bottom: 5px solid var(--edge);
    box-shadow: 0 0 0 2px var(--edge), 0 14px 30px rgba(0,0,0,.25);
    overflow: hidden;
  }
  /* front */
  .card-front { display: flex; align-items: center; }
  .brand-block {
    width: 300px; padding: 0 22px;
    display: flex; flex-direction: column; align-items: center; gap: 10px;
    text-align: center;
  }
  .brand-square { width: 34px; height: 34px; background: var(--orange); }
  .brand-name {
    color: var(--ink); font-weight: 600; font-size: 17px; letter-spacing: 1.4px;
    text-transform: uppercase; white-space: nowrap;
  }
  .brand-tagline {
    display: flex; align-items: center; gap: 10px;
    color: var(--ink); font-size: 9.5px; letter-spacing: 2px; text-transform: uppercase;
    white-space: nowrap;
  }
  .brand-tagline::before, .brand-tagline::after {
    content: ""; width: 26px; height: 1.5px; background: var(--green);
  }
  .divider { width: 1.5px; height: 210px; background: var(--muted); opacity: .7; flex: none; }
  .contact-block { padding-left: 34px; font-family: "Arimo", sans-serif; color: var(--ink); }
  .person-name { color: var(--orange); font-weight: 700; font-size: 21px; text-transform: uppercase; }
  .person-title { font-size: 15px; margin-top: 2px; }
  .address { font-size: 15px; line-height: 1.35; margin-top: 14px; }
  .contact-list { list-style: none; margin-top: 12px; font-size: 15px; line-height: 1.55; }
  .contact-list li { display: flex; align-items: center; gap: 9px; }
  .contact-list svg { width: 13px; height: 13px; flex: none; }
  /* back */
  .card-back { display: flex; align-items: center; justify-content: center; }
  .back-texture {
    position: absolute; inset: 0;
    background:
      radial-gradient(ellipse at 80% 85%, rgba(110,110,110,.55) 0%, rgba(110,110,110,0) 60%),
      linear-gradient(160deg, #161616 0%, #252525 40%, #3c3c3c 75%, #505050 100%);
  }
  .back-brand { position: relative; display: flex; flex-direction: column; align-items: center; gap: 12px; }
  .back-brand .brand-name { font-size: 28px; letter-spacing: 3px; }
  .back-brand .brand-tagline { font-size: 11px; }
</style>
</head>
<body>
  <section class="card card-front">
    <div class="brand-block">
      <span class="brand-square"></span>
      <span class="brand-name">Northfield Tax Group</span>
      <span class="brand-tagline">Solving tax problems</span>
    </div>
    <span class="divider"></span>
    <div class="contact-block">
      <p class="person-name">Daniel Harper</p>
      <p class="person-title">CEO, President</p>
      <p class="address">Your Address, City<br>State, Zip 0000</p>
      <ul class="contact-list">
        <li><svg viewBox="0 0 16 16"><path d="M4 1l3 3-2 2c1 2 3 4 5 5l2-2 3 3-2 2C7 14 2 9 2 3z" fill="none" stroke="var(--orange)" stroke-width="1.6"/></svg>555-018-2100</li>
        <li><svg viewBox="0 0 16 16"><rect x="4" y="1" width="8" height="14" rx="1.5" fill="none" stroke="var(--orange)" stroke-width="1.6"/></svg>555-018-2100</li>
        <li><svg viewBox="0 0 16 16"><rect x="1" y="3" width="14" height="10" fill="none" stroke="var(--orange)" stroke-width="1.6"/><path d="M1 3l7 6 7-6" fill="none" stroke="var(--orange)" stroke-width="1.6"/></svg>mail@northfieldtax.com</li>
        <li><svg viewBox="0 0 16 16"><circle cx="8" cy="8" r="6.5" fill="none" stroke="var(--orange)" stroke-width="1.6"/><path d="M1.5 8h13M8 1.5c-3 3-3 10 0 13M8 1.5c3 3 3 10 0 13" fill="none" stroke="var(--orange)" stroke-width="1.2"/></svg>www.northfieldtax.com</li>
      </ul>
    </div>
  </section>

  <section class="card card-back">
    <div class="back-texture" role="img" aria-label="Embossed repeating brand-symbol pattern across the whole card back, dark at top left fading to lighter grey at bottom right"></div>
    <div class="back-brand">
      <span class="brand-square"></span>
      <span class="brand-name">Northfield Tax Group</span>
      <span class="brand-tagline">Solving tax problems</span>
    </div>
  </section>
</body>
</html>
```